Marine & Offshore company business card

We need a new logo design for a new company based in Singapore called "Bovenco Global Pte. Ltd.". We are suppliers of electrical items to marine and offshore industry. We specialise in lightings, cables terminations and junction box customisation. We would like the name card to have simple modern classic look.

Target Market(s)

my target customers are ship owners, shipyard purchasers, offshore purchasers.

Industry/Entity Type

Electrical

Font styles to use
Serif
Sans Serif

Colors

Designer to choose colors to be used in the design.

```html
<!DOCTYPE html>
<html lang="en">
<head>
<meta charset="utf-8">
<title>Bovenco Global Pte. Ltd. — Business Card</title>
<link rel="stylesheet" href="https://fonts.googleapis.com/css2?family=Quicksand:wght@500;600;700&display=swap">
<style>
  :root {
    --sky: #3db5e4;
    --sky-soft: #7fd0ef;
    --ink: #1c2126;
    --paper: #ffffff;
    --backdrop: #e9ebed;
    --muted: #5f6a72;
  }
  * { box-sizing: border-box; margin: 0; padding: 0; }
  html, body { width: 1200px; height: 903px; overflow: hidden; }
  body {
    background: var(--backdrop);
    font-family: "Quicksand", "Helvetica Neue", Arial, sans-serif;
    color: var(--ink);
    display: flex;
    align-items: center;
    justify-content: center;
    gap: 40px;
  }
  .card {
    position: relative;
    width: 520px;
    height: 297px;
    background: var(--paper);
    box-shadow: 0 10px 24px rgba(0,0,0,0.18);
    overflow: hidden;
  }
  .card__shapes { position: absolute; inset: 0; }

  /* Front */
  .card--front { background: var(--sky); }
  .front__band {
    position: absolute;
    left: 0; right: 0; top: 104px; height: 89px;
    background: var(--paper);
    display: flex; align-items: center; justify-content: center; gap: 12px;
  }
  .brand__dot {
    width: 16px; height: 16px; border-radius: 50%;
    background: var(--ink);
  }
  .brand__name {
    font-weight: 700; font-size: 26px; letter-spacing: 0.5px; color: var(--ink);
  }

  /* Back */
  .back__brand {
    position: absolute; top: 22px; right: 132px;
    display: flex; align-items: center; gap: 8px;
  }
  .back__brand .brand__name { font-size: 15px; }
  .back__brand .brand__dot { width: 10px; height: 10px; }
  .person { position: absolute; left: 150px; top: 64px; }
  .person__name { font-size: 26px; font-weight: 600; }
  .person__role { font-size: 13px; font-weight: 500; color: var(--sky); letter-spacing: 1.5px; }
  .contacts {
    position: absolute; left: 28px; list-style: none;
    font-size: 11.5px; font-weight: 600; line-height: 17px;
  }
  .contacts--phones { top: 62px; }
  .contacts--info { top: 188px; }
  .contacts li { display: flex; align-items: center; gap: 6px; }
  .contacts__icon {
    width: 11px; height: 11px; background: var(--sky); color: var(--paper);
    font-size: 8px; font-weight: 700; display: inline-flex;
    align-items: center; justify-content: center; border-radius: 2px;
  }
</style>
</head>
<body>
  <section class="card card--front" aria-label="Business card front">
    <div class="front__band">
      <span class="brand__dot"></span>
      <span class="brand__name">Bovenco Global Pte. Ltd.</span>
    </div>
  </section>

  <section class="card card--back" aria-label="Business card back">
    <svg class="card__shapes" viewBox="0 0 520 297" aria-hidden="true">
      <polygon points="425,0 520,0 520,60 495,297 455,297" fill="var(--sky)"/>
      <polygon points="470,297 520,170 520,297" fill="var(--sky-soft)"/>
      <rect x="0" y="279" width="520" height="18" fill="var(--sky)"/>
    </svg>
    <div class="back__brand">
      <span class="brand__dot"></span>
      <span class="brand__name">Bovenco Global Pte. Ltd.</span>
    </div>
    <div class="person">
      <p class="person__name">Marcus Hale</p>
      <p class="person__role">Managing Director</p>
    </div>
    <ul class="contacts contacts--phones">
      <li><span class="contacts__icon">P</span>+65 6123 4870</li>
      <li><span class="contacts__icon">F</span>+65 6123 4871</li>
      <li><span class="contacts__icon">M</span>+65 9234 5618</li>
    </ul>
    <ul class="contacts contacts--info">
      <li><span class="contacts__icon">E</span>hello@bovencoglobal.sg</li>
      <li><span class="contacts__icon">W</span>www.bovencoglobal.sg</li>
      <li><span class="contacts__icon">A</span>18 Harbour Drive #04-12</li>
      <li><span class="contacts__icon" style="visibility:hidden">A</span>Singapore 117604</li>
    </ul>
  </section>
</body>
</html>
```